Business Card Design needed - Something Awesome!

Need a business card designed. Company is "Harbor Vane Consulting" we do consulting and also have sales automation technology.
I'm going to use thick stock or metal, something really nice... I was thinking about a QR Code on the back that would just upload my contact info to the persons contact, etc -

This is a Strategy Company with a tech feel. I'm open to ideas but really want this to be nice!

I need a template that should include:

Name | Position or Title
D: 555.203.8146
www.harborvaneconsulting.example

I'm going to attach my contact so you can use that one, I need to get this printed.

Target Market(s)

Small to mid size customers, Entrepreneurs etc.

Industry/Entity Type

Consulting, Tech, Private Equity.

Contact Information for Business Card

Name, Phone, Maybe email, URL

Font styles to use
Sans Serif

Colors

Designer to choose only greyscale colors for use in the design.

Requirements
Must have
• Fresh, Clean, stand out from the crowd - will be on thick stock or metal.
Nice to have
• Clean, simple yet impactful.
Should not have
• Not cartoonish

```html
<!DOCTYPE html>
<html lang="en">
<head>
<meta charset="utf-8">
<title>Harbor Vane Consulting – Business Card</title>
<link href="https://fonts.googleapis.com/css2?family=Montserrat:wght@400;600;700&display=swap" rel="stylesheet">
<style>
  :root {
    --page-top: #f2f2f2;
    --page-bottom: #4a4a4a;
    --card: #050505;
    --ink: #ffffff;
    --ink-soft: #d9d9d9;
    --rule: #bfbfbf;
  }
  * { box-sizing: border-box; margin: 0; padding: 0; }
  html, body {
    width: 1200px; height: 856px; overflow: hidden;
  }
  body {
    background: linear-gradient(180deg, var(--page-top) 0%, #bdbdbd 45%, var(--page-bottom) 100%);
    font-family: "Montserrat", sans-serif;
    color: var(--ink);
    position: relative;
  }
  .card {
    position: absolute;
    top: 279px;
    width: 520px;
    height: 298px;
    background: var(--card);
    box-shadow: 0 18px 40px rgba(0,0,0,.45);
  }
  .card--front { left: 60px; }
  .card--back { left: 620px; }

  .wordmark {
    font-weight: 600;
    letter-spacing: 0.04em;
    color: var(--ink);
    white-space: nowrap;
  }
  .card--front .wordmark {
    position: absolute;
    left: 36px;
    top: 50%;
    transform: translateY(-50%);
    font-size: 25px;
  }
  .divider {
    position: absolute;
    left: 250px;
    top: 70px;
    width: 1px;
    height: 158px;
    background: var(--rule);
  }
  .contact {
    position: absolute;
    left: 274px;
    top: 74px;
    right: 16px;
  }
  .contact__name {
    font-weight: 700;
    font-size: 17px;
    letter-spacing: 0.03em;
    text-transform: uppercase;
  }
  .contact__title {
    font-weight: 400;
    font-size: 14px;
    color: var(--ink-soft);
    margin-top: 4px;
    margin-bottom: 14px;
  }
  .contact__line {
    display: flex;
    align-items: center;
    gap: 8px;
    font-size: 13.5px;
    line-height: 1;
    margin-top: 9px;
    white-space: nowrap;
  }
  .contact__line--web { font-size: 11.5px; }
  .contact__icon { width: 13px; height: 13px; flex: none; }

  .card--back .wordmark {
    position: absolute;
    left: 0; right: 0;
    top: 50%;
    transform: translateY(-50%);
    text-align: center;
    font-size: 44px;
  }
</style>
</head>
<body>

  <section class="card card--front" aria-label="Card front">
    <div class="wordmark">HARBOR VANE</div>
    <div class="divider"></div>
    <div class="contact">
      <p class="contact__name">Dorian K. Hollis</p>
      <p class="contact__title">Founder/CEO</p>
      <p class="contact__line">
        <svg class="contact__icon" viewBox="0 0 16 16" aria-hidden="true"><path fill="#fff" d="M3.6 1.5l2.2 2.6-1.3 1.6c.9 2 2.4 3.6 4.4 4.6l1.6-1.3 2.6 2.2-1.1 2.3C7 13 3 9 1.4 3.1z"/></svg>
        555.417.2093
      </p>
      <p class="contact__line">
        <svg class="contact__icon" viewBox="0 0 16 16" aria-hidden="true"><path fill="#fff" d="M3.6 1.5l2.2 2.6-1.3 1.6c.9 2 2.4 3.6 4.4 4.6l1.6-1.3 2.6 2.2-1.1 2.3C7 13 3 9 1.4 3.1z"/></svg>
        555.203.8146
      </p>
      <p class="contact__line contact__line--web">
        <svg class="contact__icon" viewBox="0 0 16 16" aria-hidden="true"><g fill="none" stroke="#fff" stroke-width="1.3"><circle cx="8" cy="8" r="6.5"/><ellipse cx="8" cy="8" rx="2.8" ry="6.5"/><path d="M1.5 8h13"/></g></svg>
        www.harborvaneconsulting.example
      </p>
    </div>
  </section>

  <section class="card card--back" aria-label="Card back">
    <div class="wordmark">HARBOR VANE</div>
  </section>

</body>
</html>
```